Cyber Security Services Flyer/Datasheet

We are looking for a revamp of our current "Cyber Security Penetration Testing Services Datasheet". We would like a professional/modern datasheet that we can give to our Australian customers that are small to mid-sized business owners.

Please see the attached file "PLEASE READ ME.docx" for more details about the design project. It includes all of the design information. If you have more questions or would like to ask any questions please feel free to ask, we are happy to help.

```html
<!DOCTYPE html>
<html lang="en">
<head>
<meta charset="UTF-8">
<title>Penetration Testing Services Data Sheet</title>
<link href="https://fonts.googleapis.com/css2?family=Montserrat:wght@500;700;800&family=Open+Sans:ital,wght@0,400;0,600;1,400&display=swap" rel="stylesheet">
<style>
  :root{
    --stage:#0e3a48;
    --navy:#0a1a3f;
    --navy-deep:#061231;
    --navy-mid:#13285c;
    --accent:#2f8fe0;
    --accent-light:#6fc2ff;
    --ink:#1d2a4a;
    --body-text:#4a5568;
    --pale:#e9f2fb;
    --white:#ffffff;
  }
  *{box-sizing:border-box;margin:0;padding:0}
  html,body{width:833px;height:1200px;overflow:hidden;background:var(--stage)}
  .spread{position:relative;width:833px;height:1200px}
  .page{position:absolute;top:317px;width:400px;height:566px;background:var(--white);overflow:hidden;font-family:"Open Sans",sans-serif;color:var(--body-text)}
  .page--front{left:11px}
  .page--back{left:422px}

  .section-title{font-family:"Montserrat",sans-serif;font-weight:800;font-size:9px;color:var(--ink);text-transform:uppercase;line-height:1.2}
  .section-title::after{content:"";display:block;width:24px;height:2px;background:var(--accent);margin:4px 0 6px}
  .copy p{font-size:5.8px;line-height:1.55;margin-bottom:5px}

  /* front */
  .masthead{position:absolute;left:0;top:0;width:400px;height:148px;background:linear-gradient(120deg,var(--navy-deep) 0%,var(--navy) 55%,var(--navy-mid) 100%);overflow:hidden}
  .masthead__visual{position:absolute;right:-30px;top:-20px;width:190px;height:190px;border-radius:50%;background:radial-gradient(circle,#7fd4ff 0%,#2f8fe0 30%,#123a7a 62%,rgba(10,26,63,0) 72%)}
  .masthead__text{position:absolute;left:20px;top:28px;width:240px}
  .masthead__title{font-family:"Montserrat",sans-serif;font-weight:800;color:var(--white);font-size:15px;line-height:1.12;text-transform:uppercase}
  .masthead__title span{display:block;color:var(--accent-light)}
  .masthead__rule{width:34px;height:2px;background:var(--accent);margin:9px 0 7px}
  .masthead__tagline{font-family:"Montserrat",sans-serif;font-weight:700;color:var(--white);font-size:8px;line-height:1.35;width:170px}
  .intro{position:absolute;left:18px;top:160px;width:168px}
  .intro .section-title{margin-top:4px}
  .services{position:absolute;left:198px;top:156px;width:186px;height:262px;background:linear-gradient(180deg,var(--navy) 0%,var(--navy-mid) 100%);border-radius:3px;padding:14px 14px 0}
  .services .section-title{color:var(--white);font-size:10px}
  .service-list{list-style:none}
  .service-list li{display:flex;align-items:center;gap:6px;font-family:"Montserrat",sans-serif;font-weight:500;font-size:7px;color:var(--white);padding:4.5px 0;border-bottom:.5px solid rgba(255,255,255,.14)}
  .service-list svg{flex:none}
  .testimonial{margin-top:12px}
  .testimonial .section-title{color:var(--white);font-size:8px}
  .testimonial blockquote{font-style:italic;font-size:6px;line-height:1.55;color:#cfe0f5}
  .testimonial cite{display:block;margin-top:4px;font-style:normal;font-weight:600;font-size:6px;color:var(--accent-light)}
  .standards{position:absolute;left:198px;top:426px;width:186px;height:84px;background:var(--pale);border-radius:3px;padding:10px 14px}
  .standards .section-title{font-size:7.5px}
  .standards p{font-size:5.8px}
  .standards__badges{display:flex;gap:8px;margin-top:6px}
  .standards__badge{width:26px;height:20px;border-radius:3px;background:#c5d9ef}

  .brand{position:absolute;display:flex;align-items:center;gap:6px}
  .brand__mark{width:14px;height:14px;background:var(--accent)}
  .brand__name{font-family:"Montserrat",sans-serif;font-weight:800;font-size:13px;color:var(--navy);text-transform:uppercase;letter-spacing:.5px}
  .page--front .brand{left:18px;top:462px}
  .page--back .brand{left:214px;top:478px}

  .footer{position:absolute;left:0;bottom:0;width:400px;height:40px;background:var(--navy-deep);display:flex;align-items:center;padding:0 20px;gap:28px}
  .footer__item{display:flex;align-items:center;gap:5px;font-family:"Montserrat",sans-serif;font-weight:500;font-size:7px;color:var(--white)}
  .footer__icon{width:15px;height:15px;border-radius:50%;background:var(--accent);display:flex;align-items:center;justify-content:center}
  .footer--back{justify-content:flex-start}

  /* back */
  .method{position:absolute;left:0;top:0;width:400px;height:160px;background:linear-gradient(120deg,var(--navy-deep) 0%,var(--navy) 60%,var(--navy-mid) 100%);overflow:hidden}
  .method__visual{position:absolute;right:0;top:0;width:130px;height:160px;background:linear-gradient(200deg,#4aa8f0 0%,#1b4d96 45%,rgba(10,26,63,0) 100%)}
  .method__text{position:absolute;left:20px;top:22px;width:240px}
  .method__title{font-family:"Montserrat",sans-serif;font-weight:800;font-size:10px;line-height:1.2;color:var(--white);text-transform:uppercase}
  .method__title::after{content:"";display:block;width:24px;height:2px;background:var(--accent);margin:6px 0 7px}
  .method__text p{font-size:5.8px;line-height:1.55;color:#cfe0f5;margin-bottom:5px}
  .about{position:absolute;left:18px;top:174px;width:172px}
  .about .section-title,.engage .section-title{font-size:11px}
  .about__cta{font-family:"Montserrat",sans-serif;font-weight:700;font-size:7px;color:var(--ink);margin:8px 0 4px}
  .engage{position:absolute;left:206px;top:174px;width:178px}
  .steps{list-style:none;margin-top:4px}
  .steps li{display:flex;gap:5px;font-size:5.6px;line-height:1.45;margin-bottom:5px}
  .steps b{flex:none;width:10px;height:10px;border-radius:50%;background:var(--accent);color:var(--white);font-family:"Montserrat",sans-serif;font-size:5.5px;display:flex;align-items:center;justify-content:center}
  .steps strong{color:var(--ink);font-weight:600}
</style>
</head>
<body>
<div class="spread">

  <article class="page page--front">
    <header class="masthead">
      <div class="masthead__visual" role="img" aria-label="Glowing digital globe with network lines"></div>
      <div class="masthead__text">
        <h1 class="masthead__title">Penetration Testing Services<span>Data Sheet</span></h1>
        <div class="masthead__rule"></div>
        <p class="masthead__tagline">Affordable Security Assessments To Suit Your Business Requirements</p>
      </div>
    </header>

    <section class="intro copy">
      <h2 class="section-title">What is Penetration Testing</h2>
      <p>Penetration testing is the process of simulating real-world attacks against your systems to find weaknesses before criminals do. Our certified testers use the same tools and techniques as attackers, working within agreed boundaries so daily operations are never put at risk.</p>
      <p>Every engagement ends with a clear report that ranks each finding by risk and explains in plain language how to fix it, so your team knows where to focus time and budget.</p>
      <h2 class="section-title">Why Penetration Testing</h2>
      <p>Small and mid-sized businesses are now prime targets because attackers expect weaker defences. Regular testing shows how an intruder could move through your network and proves that existing controls work.</p>
      <p>Testing also helps you meet client, insurer and regulatory expectations, and shows partners that you take the protection of their data seriously.</p>
    </section>

    <section class="services">
      <h2 class="section-title">Our Services</h2>
      <ul class="service-list">
        <li><svg width="10" height="10" viewBox="0 0 20 20"><circle cx="10" cy="10" r="10" fill="#2f8fe0"/><path d="M5.5 10.5l3 3 6-6.5" stroke="#fff" stroke-width="2.4" fill="none"/></svg>External Network Testing</li>
        <li><svg width="10" height="10" viewBox="0 0 20 20"><circle cx="10" cy="10" r="10" fill="#2f8fe0"/><path d="M5.5 10.5l3 3 6-6.5" stroke="#fff" stroke-width="2.4" fill="none"/></svg>Phishing Testing and Awareness Training</li>
        <li><svg width="10" height="10" viewBox="0 0 20 20"><circle cx="10" cy="10" r="10" fill="#2f8fe0"/><path d="M5.5 10.5l3 3 6-6.5" stroke="#fff" stroke-width="2.4" fill="none"/></svg>Wireless Network Testing</li>
        <li><svg width="10" height="10" viewBox="0 0 20 20"><circle cx="10" cy="10" r="10" fill="#2f8fe0"/><path d="M5.5 10.5l3 3 6-6.5" stroke="#fff" stroke-width="2.4" fill="none"/></svg>Internal Network Testing</li>
        <li><svg width="10" height="10" viewBox="0 0 20 20"><circle cx="10" cy="10" r="10" fill="#2f8fe0"/><path d="M5.5 10.5l3 3 6-6.5" stroke="#fff" stroke-width="2.4" fill="none"/></svg>Security Vulnerability Assessments</li>
        <li><svg width="10" height="10" viewBox="0 0 20 20"><circle cx="10" cy="10" r="10" fill="#2f8fe0"/><path d="M5.5 10.5l3 3 6-6.5" stroke="#fff" stroke-width="2.4" fill="none"/></svg>Web Application Testing</li>
      </ul>
      <div class="testimonial">
        <h2 class="section-title">What Clients Say About Us</h2>
        <blockquote>“The team found issues our previous provider missed and explained every step clearly. We now test twice a year and feel far more prepared.”</blockquote>
        <cite>Operations Manager, Brisbane</cite>
      </div>
    </section>

    <section class="standards">
      <h2 class="section-title">Our Cybersecurity Standards</h2>
      <p>Our testing follows recognised industry frameworks.</p>
      <div class="standards__badges">
        <div class="standards__badge"></div>
        <div class="standards__badge"></div>
        <div class="standards__badge"></div>
        <div class="standards__badge"></div>
      </div>
    </section>

    <div class="brand">
      <div class="brand__mark"></div>
      <div class="brand__name">Bastion Secure</div>
    </div>

    <footer class="footer">
      <div class="footer__item">
        <span class="footer__icon"><svg width="8" height="6" viewBox="0 0 16 12"><rect x="0.75" y="0.75" width="14.5" height="10.5" rx="1.5" fill="none" stroke="#fff" stroke-width="1.8"/><path d="M1 1.5l7 5 7-5" fill="none" stroke="#fff" stroke-width="1.8"/></svg></span>
        hello@bastionsecure.com.au
      </div>
      <div class="footer__item">
        <span class="footer__icon"><svg width="8" height="8" viewBox="0 0 16 16"><circle cx="8" cy="8" r="7" fill="none" stroke="#fff" stroke-width="1.6"/><ellipse cx="8" cy="8" rx="3" ry="7" fill="none" stroke="#fff" stroke-width="1.4"/><path d="M1 8h14" stroke="#fff" stroke-width="1.4"/></svg></span>
        bastionsecure.com.au
      </div>
    </footer>
  </article>

  <article class="page page--back">
    <header class="method">
      <div class="method__visual" role="img" aria-label="Hands typing on a laptop with glowing security graphics"></div>
      <div class="method__text">
        <h2 class="method__title">Our External Penetration Testing Methodology</h2>
        <p>Our external testing follows a structured path: reconnaissance, discovery, vulnerability analysis, controlled exploitation and reporting. We map everything an attacker can see from the internet, then safely confirm which weaknesses could actually be used to gain entry.</p>
        <p>Each stage is agreed with you in advance, and results are reviewed by a senior tester before delivery so findings are accurate and free of noise.</p>
      </div>
    </header>

    <section class="about copy">
      <h2 class="section-title">About Us</h2>
      <p>We are an Australian security consultancy helping small and mid-sized organisations understand and reduce their cyber risk. Our testers hold respected industry certifications and bring years of hands-on experience across finance, health, retail and government.</p>
      <p>We believe strong security should be affordable. That is why our services are scoped to your size and budget, with no lock-in contracts and no jargon-filled reports.</p>
      <p>From a single web application to a full network review, we work alongside your team and stay available after testing to answer questions and verify fixes.</p>
      <p class="about__cta">See How We Can Secure Your Assets</p>
      <p>Contact us today for an obligation-free discussion and a fixed-price proposal tailored to your business.</p>
    </section>

    <section class="engage copy">
      <h2 class="section-title">Client Engagement Process</h2>
      <p>Our simple process keeps you informed from first call to final report.</p>
      <ol class="steps">
        <li><b>1</b><span><strong>Consult</strong> – we discuss your goals, systems and concerns.</span></li>
        <li><b>2</b><span><strong>Scope</strong> – we agree targets, timing and a fixed quote.</span></li>
        <li><b>3</b><span><strong>Test</strong> – our team performs the assessment safely.</span></li>
        <li><b>4</b><span><strong>Report</strong> – you receive clear, ranked findings.</span></li>
        <li><b>5</b><span><strong>Debrief</strong> – we walk through results and fixes.</span></li>
        <li><b>6</b><span><strong>Retest</strong> – we confirm issues are resolved.</span></li>
      </ol>
    </section>

    <div class="brand">
      <div class="brand__mark"></div>
      <div class="brand__name">Bastion Secure</div>
    </div>

    <footer class="footer footer--back">
      <div class="footer__item">
        <span class="footer__icon"><svg width="8" height="6" viewBox="0 0 16 12"><rect x="0.75" y="0.75" width="14.5" height="10.5" rx="1.5" fill="none" stroke="#fff" stroke-width="1.8"/><path d="M1 1.5l7 5 7-5" fill="none" stroke="#fff" stroke-width="1.8"/></svg></span>
        hello@bastionsecure.com.au
      </div>
      <div class="footer__item">
        <span class="footer__icon"><svg width="8" height="8" viewBox="0 0 16 16"><circle cx="8" cy="8" r="7" fill="none" stroke="#fff" stroke-width="1.6"/><ellipse cx="8" cy="8" rx="3" ry="7" fill="none" stroke="#fff" stroke-width="1.4"/><path d="M1 8h14" stroke="#fff" stroke-width="1.4"/></svg></span>
        bastionsecure.com.au
      </div>
    </footer>
  </article>

</div>
</body>
</html>
```